12 page New Church Launch Booklet

I have a 12 page 8.5x11 Mock-up of a Launch booklet I need to get done and made ready to be sent to Pressloft.com for printing. I have uploaded the 12 pages and the content that I need. I need to have this designed from scratch while being inspired by the mock-up. I am open to new concepts and design ideas from the designer. I would like to use some of the pictures that are included in the mock-up but if there are other options that will work better i am open to that.

Target Market(s)

Churches who support church plants and individuals who may be interested in joining the launch team.

Font styles to use
Serif

Colors

Designer to choose colors to be used in the design.

Requirements
Must have
• I have uploaded a mock-up. i just want something that will be appealing to the eye.

```html
<!DOCTYPE html>
<html lang="en">
<head>
<meta charset="utf-8">
<title>Riverbend Church Launch Booklet</title>
<link rel="stylesheet" href="https://fonts.googleapis.com/css2?family=Montserrat:wght@400;600;700;800&family=Open+Sans:wght@400;600;700&display=swap">
<style>
:root{
  --red:#c0141b;
  --red-dark:#7d0c10;
  --orange:#e2822b;
  --ink:#222;
  --grey:#d9d9d9;
  --grey-light:#eeeeee;
  --charcoal:#262626;
  --navy:#0d1b33;
  --white:#fff;
  --bg:#ffffff;
}
*{box-sizing:border-box;margin:0;padding:0}
html,body{width:1200px;height:1200px;overflow:hidden;background:var(--bg)}
body{position:relative;font-family:"Open Sans",Arial,sans-serif;color:var(--ink)}
.spread{position:absolute;width:476px;height:330px;overflow:hidden;box-shadow:0 2px 6px rgba(0,0,0,.25)}
.page{position:absolute;top:0;width:238px;height:330px;overflow:hidden}
.page.left{left:0}.page.right{left:238px}
.abs{position:absolute}
.photo{position:absolute}
.runhead{position:absolute;top:6px;font:600 5px "Montserrat",sans-serif;color:var(--red);white-space:nowrap}
.runline{position:absolute;top:9px;height:.6px;background:var(--red)}
.h{font-family:"Montserrat",sans-serif;font-weight:800;letter-spacing:.5px}
.body{font-size:3.6px;line-height:4.6px;text-align:justify;color:#333}
.body.light{color:#eee}
.list{list-style:none}
.list li{display:flex;gap:3px;align-items:flex-start;margin-bottom:3.5px}
.tick{flex:0 0 6px;width:6px;height:6px}
.brand{font-family:"Montserrat",sans-serif;font-weight:700;white-space:nowrap}
.quotebox{position:absolute;border:1px solid currentColor;border-radius:5px;text-align:center;font-family:"Montserrat",sans-serif}
.redbar{position:absolute;left:0;bottom:0;width:476px;height:9px;background:var(--red)}
</style>
</head>
<body>

<!-- Spread 1: covers -->
<section class="spread cover" style="left:102px;top:48px;background:var(--charcoal)">
  <div class="photo" role="img" aria-label="Black and white photo of hands playing an acoustic guitar" style="left:0;top:0;width:238px;height:260px;background:linear-gradient(160deg,#3a3a3a,#6d6d6d 55%,#2a2a2a)"></div>
  <div class="photo" role="img" aria-label="Black and white photo of a worship crowd with raised hands" style="left:238px;top:90px;width:238px;height:180px;background:linear-gradient(180deg,#1e1e1e,#8a8a8a 55%,#3a3a3a)"></div>
  <svg class="abs" style="left:0;top:0" width="476" height="330" viewBox="0 0 476 330">
    <path d="M0 225 C120 250 200 262 238 270 C320 255 400 240 476 228 L476 250 C400 262 320 276 238 292 C180 280 90 265 0 250 Z" fill="var(--orange)"/>
    <path d="M0 250 C90 265 180 280 238 292 C320 276 400 262 476 250 L476 330 L0 330 Z" fill="#1b1b1b"/>
  </svg>
  <div class="abs h" style="left:78px;top:58px;font-size:16px;color:var(--orange);transform:rotate(-4deg)">LAUNCHING</div>
  <div class="abs" style="left:88px;top:78px;font:600 10px Montserrat,sans-serif;color:#cfcfcf;transform:rotate(-4deg);letter-spacing:1px">EASTER 2020</div>
  <div class="abs brand" style="left:78px;top:300px;font-size:11px;color:var(--white)">Riverbend Church</div>
  <div class="abs brand" style="left:292px;top:36px;font-size:19px;color:var(--white)">Riverbend</div>
  <div class="abs brand" style="left:336px;top:60px;font-size:10px;color:var(--orange);letter-spacing:2px">CHURCH</div>
  <div class="abs h" style="left:272px;top:298px;font-size:9px;color:var(--orange)">LAUNCHING APRIL 12, 2020</div>
  <div class="abs" style="left:290px;top:312px;font:600 3.8px Montserrat,sans-serif;color:#ddd;letter-spacing:.4px">"A MULTI-ETHNIC CHURCH PLANTING CHURCH"</div>
</section>

<!-- Spread 2: meet the planter -->
<section class="spread planter" style="left:616px;top:48px;background:linear-gradient(90deg,#e6e6e6,#f5f5f5 50%,#e4e4e4)">
  <div class="page left">
    <span class="runhead" style="left:10px">Riverbend Church</span><span class="runline" style="left:60px;width:178px"></span>
    <div class="photo" role="img" aria-label="Photo of the church planter standing in a black polo shirt" style="left:0;top:20px;width:140px;height:300px;background:linear-gradient(180deg,#cfcfcf,#3a3a3a 35%,#1a1a1a 70%,#34425a)"></div>
    <div class="abs" style="left:140px;top:20px;width:98px;height:88px;background:var(--red)">
      <div class="h" style="position:absolute;left:6px;top:18px;font-size:10px;font-weight:600;color:#fff">I AM</div>
      <div class="h" style="position:absolute;left:6px;top:28px;font-size:17px;color:#fff">DARNELL</div>
      <div style="position:absolute;left:7px;top:51px;font:600 4.5px Montserrat,sans-serif;color:#fff">CHURCH PLANTER</div>
    </div>
    <p class="abs body" style="left:144px;top:112px;width:88px">Darnell Hayes was born and raised as a preacher's kid in the central city of Lakeport. As a youth, he was involved with gangs and by the age of 22 was a successful drug dealer. After a near death experience, he gave his life to Jesus and would later become an ordained minister. In 2005, he planted his first church in the central city of Lakeport. In 2016, he led the launch of a north side multi-ethnic ministry initiative for a partner church. He and his wife Renee are the proud parents of 5 adult children and the proud grandparents of 10.</p>
    <div class="abs h" style="left:144px;top:218px;font-size:6.5px;color:var(--red)">EDUCATION</div>
    <div class="abs" style="left:144px;top:229px;width:90px;font-size:3.8px;line-height:4.6px;color:#333">
      <p>• <b>B.A. in Business</b><br>&nbsp;&nbsp;from Northfield College</p><br>
      <p>• <b>M.A. in Christian Ministry</b><br>&nbsp;&nbsp;from Grace Hill Seminary</p><br>
      <p>• <b>Ed. D in Organizational Leadership (ABD)</b><br>&nbsp;&nbsp;from Westmere University</p>
    </div>
  </div>
  <div class="page right">
    <span class="runhead" style="left:168px">Riverbend Church</span><span class="runline" style="left:0;width:164px"></span>
    <div class="abs" style="left:0;top:20px;width:238px;height:82px;background:var(--red)"></div>
    <div class="photo" role="img" aria-label="Photo of two men talking over coffee in a cafe" style="left:25px;top:24px;width:168px;height:74px;background:linear-gradient(135deg,#8b7a6a,#d8cbbd 50%,#4b3d33)"></div>
    <div class="abs h" style="left:16px;top:118px;font-size:11px;line-height:11px;color:#222">COMMUNITY<br><span style="color:var(--red)">CONNECTION</span></div>
    <ul class="abs list" style="left:16px;top:148px;width:90px;font-size:4px;line-height:4.6px;color:#333">
      <li><svg class="tick" viewBox="0 0 10 10"><circle cx="5" cy="5" r="4.3" fill="none" stroke="#c0141b" stroke-width="1.2"/><path d="M3 5.2l1.5 1.5L7.2 3.6" fill="none" stroke="#c0141b" stroke-width="1.2"/></svg><span>Board member of Harbor Supply and Open Door Partners</span></li>
      <li><svg class="tick" viewBox="0 0 10 10"><circle cx="5" cy="5" r="4.3" fill="none" stroke="#c0141b" stroke-width="1.2"/><path d="M3 5.2l1.5 1.5L7.2 3.6" fill="none" stroke="#c0141b" stroke-width="1.2"/></svg><span>Board member of Eastgate High School</span></li>
      <li><svg class="tick" viewBox="0 0 10 10"><circle cx="5" cy="5" r="4.3" fill="none" stroke="#c0141b" stroke-width="1.2"/><path d="M3 5.2l1.5 1.5L7.2 3.6" fill="none" stroke="#c0141b" stroke-width="1.2"/></svg><span>Member of Steering Council of Lakeside Health Network</span></li>
      <li><svg class="tick" viewBox="0 0 10 10"><circle cx="5" cy="5" r="4.3" fill="none" stroke="#c0141b" stroke-width="1.2"/><path d="M3 5.2l1.5 1.5L7.2 3.6" fill="none" stroke="#c0141b" stroke-width="1.2"/></svg><span>Founder and president of Common Ground Builders, a neighborhood development organization</span></li>
      <li><svg class="tick" viewBox="0 0 10 10"><circle cx="5" cy="5" r="4.3" fill="none" stroke="#c0141b" stroke-width="1.2"/><path d="M3 5.2l1.5 1.5L7.2 3.6" fill="none" stroke="#c0141b" stroke-width="1.2"/></svg><span>President of the Lakeport Covenant, a group of multi-ethnic pastors who stand as one in promoting racial unity within the body of Christ.</span></li>
    </ul>
    <div class="photo" role="img" aria-label="Photo of the church planter and his wife standing together" style="left:112px;top:105px;width:122px;height:215px;background:linear-gradient(180deg,#d8d8d8,#2c3a78 45%,#1d2440 80%,#8a1d1d)"></div>
  </div>
  <div class="redbar"></div>
</section>

<!-- Spread 3: my story -->
<section class="spread story" style="left:102px;top:436px;background:linear-gradient(90deg,#e8e8e8,#f4f4f4 50%,#e6e6e6)">
  <div class="abs" style="left:0;top:0;width:476px;height:52px;background:linear-gradient(180deg,var(--red),var(--red-dark))"></div>
  <span class="runhead" style="left:10px;color:#fff">Riverbend Church</span>
  <span class="runhead" style="left:406px;color:#fff">Riverbend Church</span>
  <div class="abs h" style="left:78px;top:32px;font-size:13px;color:#fff">MY STORY</div>
  <div class="photo" role="img" aria-label="Black and white photo of a city street lined with houses" style="left:0;top:52px;width:476px;height:98px;background:linear-gradient(180deg,#bdbdbd,#8c8c8c 60%,#d6d6d6)"></div>
  <p class="abs body" style="left:12px;top:146px;width:194px">In spite of being a pastor's kid, I felt as if I was doomed to fail. I never understood why I had to beg God for acceptance, so I gave up and turned to the streets of Lakeport. As a successful dealer, my peers more than accepted me. I wore the best clothes, drove the best cars, made a ton of money, and simply purchased acceptance from others. Nevertheless, my lavish lifestyle also made me a target. I was robbed three separate times, but it wasn't until the last robbery at gunpoint that I truly began considering life after death. As the gunman demanded I kneel down, I figured I only had enough time left to ask God to forgive me, which I did. Surprised I was still alive, I then promised God that if he got me out of that situation, I would change my life.</p>
  <div class="abs h" style="left:68px;top:234px;font-size:9px;color:var(--red)">SPARED BY GOD</div>
  <p class="abs body" style="left:12px;top:248px;width:218px">All in one swoop, I flipped my body off the porch while landing on my shoeless feet. While there is no reasonable explanation of how that was possible, God not only heard my plea but spared my life that day. I was forever changed! From that day forward, I was determined to keep my vow to the Lord. I completely turned away from my life as a dealer, and took a job working as a delivery driver for a pharmacy company making $7.50 an hour. It was still delivering drugs but this time it was legit and for a lot less money. My first life lesson in humility! A young man on the job took a keen interest in me and began teaching me the business, and from there into the front office.</p>
  <div class="photo" role="img" aria-label="Photo of a pastor preaching on a stage with a screen and cross behind him" style="left:202px;top:136px;width:130px;height:82px;border-radius:5px;border:2px solid #fff;background:linear-gradient(180deg,#0f1a2a,#3c5a2a 45%,#1a1a1a)"></div>
  <div class="quotebox" style="left:340px;top:156px;width:124px;height:50px;color:var(--red)">
    <div class="h" style="position:absolute;left:6px;top:-10px;font-size:16px">“</div>
    <div style="position:absolute;left:4px;right:4px;top:12px;font:600 5px/6px Montserrat,sans-serif;color:#333">I VALUE MULTI-ETHNIC MINISTRY BECAUSE I AM THE PRODUCT OF WHAT CAN HAPPEN THROUGH MULTI-ETHNIC RELATIONSHIPS</div>
    <div class="h" style="position:absolute;right:6px;bottom:-14px;font-size:16px">”</div>
  </div>
  <div class="abs" style="left:348px;top:213px;font:italic 4px Montserrat,sans-serif;color:var(--red)">- Darnell Hayes</div>
  <p class="abs body" style="left:250px;top:236px;width:216px">I had worked my way up to the top of that branch. A couple of months later, I was promoted to our corporate office. Unbelievably, in a period of 18 months I had gone from being a street dealer to running 13 branches nationwide, albeit with no college education. By this time, I knew God was at work in my life. Soon after arriving, an older gentleman knocked at my door. He said he wanted to share the Gospel. I remember him asking me "If you were to die tonight and sat at God's door, what would you say to him to let you in?" I said something along the lines of my good outweighing my bad. He informed me that salvation had nothing to do with what I had done in life. That night I tossed and turned wondering how that scripture could be true. Tears flowed like a well spring when it finally hit me. Ironically, the moral of my story is the two most important life moments came through multi-ethnic interaction.</p>
  <div class="redbar"></div>
</section>

<!-- Spread 4: problem and solution -->
<section class="spread problem" style="left:616px;top:436px;background:#1d1d1d">
  <div class="page left" style="background:#eee">
    <span class="runhead" style="left:10px;color:#fff">Riverbend Church</span>
    <div class="photo" role="img" aria-label="Black and white photo of a corner store on an urban street" style="left:0;top:0;width:110px;height:330px;background:linear-gradient(160deg,#f0f0f0,#9a9a9a 40%,#4a4a4a 75%,#bbb)"></div>
    <div class="abs" style="left:110px;top:0;width:128px;height:330px;background:linear-gradient(180deg,var(--red),var(--red-dark))">
      <div class="h" style="position:absolute;left:0;right:0;top:50px;text-align:center;font-size:11px;line-height:13px;color:#fff">THE<br>PROBLEM</div>
      <p class="body light" style="position:absolute;left:12px;top:100px;width:104px">In spite of being a pastor's kid, I felt as if I was doomed to fail. I never understood why I had to beg God for acceptance, so I gave up and turned to the streets of Lakeport. As a successful dealer, my peers more than accepted me. I wore the best clothes, drove the best cars, made a ton of money, and simply purchased acceptance and validation from others. Nevertheless, my lavish lifestyle also made me a target. I was robbed three separate times, but it wasn't until the last robbery at gunpoint that I truly began considering life after death. As the gunman demanded I kneel down, I figured I only had enough time left to ask God to forgive me, which I did. Surprised I was still alive, I then promised God if he got me out of that situation, I would change my life. In a strange twist of fate, the gunman did not pull the trigger and instead demanded I lead them to the money. Therefore, I led them to the upper porch of my home and reached underneath the banister as though I had money hidden there.</p>
    </div>
  </div>
  <div class="page right" style="background:linear-gradient(180deg,#3a3a3a,#1d1d1d 55%)">
    <span class="runhead" style="left:168px;color:#fff">Riverbend Church</span>
    <div class="h" style="position:absolute;left:0;right:0;top:32px;text-align:center;font-size:11px;color:#fff">THE SOLUTION</div>
    <svg class="abs" style="left:70px;top:50px" width="98" height="18" viewBox="0 0 98 18" fill="#ddd">
      <g><rect x="4" y="8" width="8" height="9"/><path d="M3 9L8 4L13 9Z"/><rect x="7.5" y="0" width="1" height="4"/></g>
      <g transform="translate(20 0)"><rect x="4" y="8" width="8" height="9"/><path d="M3 9L8 4L13 9Z"/><rect x="7.5" y="0" width="1" height="4"/></g>
      <g transform="translate(40 -1) scale(1.15)"><rect x="3" y="8" width="10" height="8"/><path d="M2 9L8 3L14 9Z"/><rect x="7.5" y="0" width="1" height="3"/></g>
      <g transform="translate(62 0)"><rect x="4" y="8" width="8" height="9"/><path d="M3 9L8 4L13 9Z"/><rect x="7.5" y="0" width="1" height="4"/></g>
      <g transform="translate(82 0)"><rect x="4" y="8" width="8" height="9"/><path d="M3 9L8 4L13 9Z"/><rect x="7.5" y="0" width="1" height="4"/></g>
    </svg>
    <div class="abs" style="left:30px;top:70px;width:178px;height:.6px;background:#888"></div>
    <div class="abs h" style="left:10px;top:72px;font-size:20px;color:var(--red)">“</div>
    <div class="abs" style="left:30px;top:74px;width:178px;text-align:center;font:400 8px/9px Montserrat,sans-serif;color:#fff">PLANT <b>FIVE</b> CHURCHES<br>IN THE NEXT <b>FIVE</b> YEARS</div>
    <div class="abs h" style="left:212px;top:72px;font-size:20px;color:var(--red)">”</div>
    <div class="abs" style="left:30px;top:95px;width:178px;height:.6px;background:#888"></div>
    <p class="abs" style="left:24px;top:104px;width:190px;text-align:center;font:600 3.4px/4.4px 'Open Sans',sans-serif;color:#eee">In conjunction with Metro Church Planters, Riverbend will plant five churches over the next five years. Be that as it may, and in an effort to address the lack of church planting in Lakeport, a culture of church planting among Black church communities in partnership with suburban churches must be built.</p>
    <div class="photo" role="img" aria-label="Red toned photo of a worship crowd with raised hands" style="left:0;top:175px;width:238px;height:155px;background:linear-gradient(180deg,#c0141b,#7d0c10 60%,#2a0506)"></div>
    <div class="abs" style="left:32px;top:160px;width:174px;height:8px;background:#111;text-align:center;font:700 4.5px/8px Montserrat,sans-serif;color:#fff">KEYS TO SUCCESS</div>
    <ul class="abs list" style="left:42px;top:174px;width:160px;font-size:3.6px;line-height:4.2px;color:#f2f2f2">
      <li><svg class="tick" viewBox="0 0 10 10"><circle cx="5" cy="5" r="4.3" fill="none" stroke="#fff" stroke-width="1.2"/><path d="M3 5.2l1.5 1.5L7.2 3.6" fill="none" stroke="#fff" stroke-width="1.2"/></svg><span>Create new assessments best defining the characteristics needed for a central city church planter</span></li>
      <li><svg class="tick" viewBox="0 0 10 10"><circle cx="5" cy="5" r="4.3" fill="none" stroke="#fff" stroke-width="1.2"/><path d="M3 5.2l1.5 1.5L7.2 3.6" fill="none" stroke="#fff" stroke-width="1.2"/></svg><span>Build strong central city church planting network</span></li>
      <li><svg class="tick" viewBox="0 0 10 10"><circle cx="5" cy="5" r="4.3" fill="none" stroke="#fff" stroke-width="1.2"/><path d="M3 5.2l1.5 1.5L7.2 3.6" fill="none" stroke="#fff" stroke-width="1.2"/></svg><span>Create urban/suburban church planting partnerships</span></li>
      <li><svg class="tick" viewBox="0 0 10 10"><circle cx="5" cy="5" r="4.3" fill="none" stroke="#fff" stroke-width="1.2"/><path d="M3 5.2l1.5 1.5L7.2 3.6" fill="none" stroke="#fff" stroke-width="1.2"/></svg><span>Plant churches that plant churches</span></li>
      <li><svg class="tick" viewBox="0 0 10 10"><circle cx="5" cy="5" r="4.3" fill="none" stroke="#fff" stroke-width="1.2"/><path d="M3 5.2l1.5 1.5L7.2 3.6" fill="none" stroke="#fff" stroke-width="1.2"/></svg><span>Identify and equip indigenous central-city church planters</span></li>
      <li><svg class="tick" viewBox="0 0 10 10"><circle cx="5" cy="5" r="4.3" fill="none" stroke="#fff" stroke-width="1.2"/><path d="M3 5.2l1.5 1.5L7.2 3.6" fill="none" stroke="#fff" stroke-width="1.2"/></svg><span>Establish a contextualized funding model</span></li>
    </ul>
  </div>
</section>

<!-- Spread 5: mission and discipleship -->
<section class="spread mission" style="left:102px;top:812px;background:linear-gradient(90deg,#e4e4e4,#f3f3f3 50%,#e4e4e4)">
  <div class="page left">
    <span class="runhead" style="left:10px">Riverbend Church</span><span class="runline" style="left:60px;width:178px"></span>
    <div class="abs h" style="left:0;right:0;top:22px;text-align:center;font-size:13px;color:var(--red)">MISSION</div>
    <div class="abs" style="left:0;top:44px;width:238px;height:52px;background:linear-gradient(180deg,var(--red),var(--red-dark))"></div>
    <div class="quotebox" style="left:30px;top:50px;width:178px;height:38px;color:#fff">
      <div class="h" style="position:absolute;left:8px;top:-12px;font-size:16px">“</div>
      <div style="position:absolute;left:6px;right:6px;top:7px;font:600 6.2px/7.6px Montserrat,sans-serif">To be a gospel centered, multi-ethnic, church planting church built on the pillars of missions, faith, work, and economics</div>
      <div class="h" style="position:absolute;right:8px;bottom:-15px;font-size:16px">”</div>
    </div>
    <div class="photo" role="img" aria-label="Faded black and white photo of a congregation" style="left:0;top:250px;width:238px;height:80px;background:linear-gradient(180deg,rgba(200,200,200,0),#6a6a6a)"></div>
    <div class="abs h" style="left:18px;top:108px;font-size:4.8px;line-height:5.6px;color:var(--red)">WHAT'S THE GIST BEHIND<br>THE FOUR PILLARS</div>
    <p class="abs" style="left:18px;top:124px;width:92px;font:600 3.6px/4.8px 'Open Sans',sans-serif;color:#333">The gist of our mission is to build out ministry in a way where we don't add another thing to the lives of our people but rather, we seek to be a part of what is already happening in the lives of those we serve. Therefore, we intend to embrace the local mission efforts that already exist in our community. We will explore how we can best support our brothers and sisters doing parachurch ministry sitting in our pews. Additionally, our desire is to see the faith community equipped with a biblical theology of work and economics so we might contribute to making a sustainable impact on human flourishing in our community.</p>
    <div class="abs h" style="left:124px;top:110px;font-size:7px;color:var(--red)">CORE VALUES</div>
    <ul class="abs list" style="left:124px;top:124px;width:110px;font:600 4px/4.6px Montserrat,sans-serif;color:#333">
      <li><svg class="tick" viewBox="0 0 10 10"><circle cx="5" cy="5" r="4.3" fill="none" stroke="#333" stroke-width="1.2"/><path d="M3 5.2l1.5 1.5L7.2 3.6" fill="none" stroke="#333" stroke-width="1.2"/></svg><span>BIBLICALLY CENTERED TEACHING</span></li>
      <li><svg class="tick" viewBox="0 0 10 10"><circle cx="5" cy="5" r="4.3" fill="none" stroke="#333" stroke-width="1.2"/><path d="M3 5.2l1.5 1.5L7.2 3.6" fill="none" stroke="#333" stroke-width="1.2"/></svg><span>DIVERSITY</span></li>
      <li><svg class="tick" viewBox="0 0 10 10"><circle cx="5" cy="5" r="4.3" fill="none" stroke="#333" stroke-width="1.2"/><path d="M3 5.2l1.5 1.5L7.2 3.6" fill="none" stroke="#333" stroke-width="1.2"/></svg><span>AUTHENTICITY</span></li>
      <li><svg class="tick" viewBox="0 0 10 10"><circle cx="5" cy="5" r="4.3" fill="none" stroke="#333" stroke-width="1.2"/><path d="M3 5.2l1.5 1.5L7.2 3.6" fill="none" stroke="#333" stroke-width="1.2"/></svg><span>VULNERABILITY</span></li>
      <li><svg class="tick" viewBox="0 0 10 10"><circle cx="5" cy="5" r="4.3" fill="none" stroke="#333" stroke-width="1.2"/><path d="M3 5.2l1.5 1.5L7.2 3.6" fill="none" stroke="#333" stroke-width="1.2"/></svg><span>CHURCH PLANTING</span></li>
      <li><svg class="tick" viewBox="0 0 10 10"><circle cx="5" cy="5" r="4.3" fill="none" stroke="#333" stroke-width="1.2"/><path d="M3 5.2l1.5 1.5L7.2 3.6" fill="none" stroke="#333" stroke-width="1.2"/></svg><span>THE UNBELIEVER</span></li>
      <li><svg class="tick" viewBox="0 0 10 10"><circle cx="5" cy="5" r="4.3" fill="none" stroke="#333" stroke-width="1.2"/><path d="M3 5.2l1.5 1.5L7.2 3.6" fill="none" stroke="#333" stroke-width="1.2"/></svg><span>LOCAL MISSIONS</span></li>
      <li><svg class="tick" viewBox="0 0 10 10"><circle cx="5" cy="5" r="4.3" fill="none" stroke="#333" stroke-width="1.2"/><path d="M3 5.2l1.5 1.5L7.2 3.6" fill="none" stroke="#333" stroke-width="1.2"/></svg><span>LIFE GROUPS &amp; COMMUNITY</span></li>
      <li><svg class="tick" viewBox="0 0 10 10"><circle cx="5" cy="5" r="4.3" fill="none" stroke="#333" stroke-width="1.2"/><path d="M3 5.2l1.5 1.5L7.2 3.6" fill="none" stroke="#333" stroke-width="1.2"/></svg><span>UNCONDITIONAL LOVE</span></li>
      <li><svg class="tick" viewBox="0 0 10 10"><circle cx="5" cy="5" r="4.3" fill="none" stroke="#333" stroke-width="1.2"/><path d="M3 5.2l1.5 1.5L7.2 3.6" fill="none" stroke="#333" stroke-width="1.2"/></svg><span>HUMAN FLOURISHING</span></li>
    </ul>
  </div>
  <div class="page right">
    <span class="runhead" style="left:168px">Riverbend Church</span><span class="runline" style="left:0;width:164px"></span>
    <div class="abs h" style="left:0;right:0;top:26px;text-align:center;font-size:13px;color:var(--red)">DISCIPLESHIP</div>
    <div class="abs" style="left:0;top:44px;width:238px;height:52px;background:var(--red)"></div>
    <div class="photo" role="img" aria-label="Warm toned photo of worshippers with raised hands" style="left:12px;top:44px;width:214px;height:52px;background:linear-gradient(180deg,#d9a27a,#8a3a22 55%,#3a1410)"></div>
    <svg class="abs" style="left:36px;top:104px" width="110" height="130" viewBox="0 0 110 130">
      <path d="M4 70 C30 35 70 18 104 20" fill="none" stroke="#c0141b" stroke-width="3"/>
      <path d="M96 13 L108 20 L96 27 Z" fill="#c0141b"/>
      <rect x="14" y="82" width="14" height="46" fill="#c0141b"/>
      <rect x="32" y="68" width="14" height="60" fill="#c0141b"/>
      <rect x="50" y="54" width="14" height="74" fill="#c0141b"/>
      <rect x="68" y="40" width="14" height="88" fill="#c0141b"/>
      <g font-family="Montserrat,sans-serif" font-weight="800" font-size="9" fill="#222">
        <text transform="translate(24 126) rotate(-90)">FAITH</text>
        <text transform="translate(42 126) rotate(-90)">FELLOWSHIP</text>
        <text transform="translate(60 126) rotate(-90)">FOLLOW</text>
        <text transform="translate(78 126) rotate(-90)">FLOURISH</text>
      </g>
    </svg>
    <div class="abs" style="left:150px;top:112px;width:82px;font-size:3.4px;line-height:4px;color:#333">
      <p><span style="background:var(--red);color:#fff;font-weight:700;padding:0 2px">STEP ONE:</span><br>We invite people to FAITH in Jesus.</p><br>
      <p><span style="background:var(--red);color:#fff;font-weight:700;padding:0 2px">STEP TWO</span><br>We invite people into FELLOWSHIP.<br>1. Worship<br>2. Life Groups<br>3. Community</p><br>
      <p><span style="background:var(--red);color:#fff;font-weight:700;padding:0 2px">STEP THREE</span><br>We inspire people to FOLLOW the teachings of Jesus.<br>• Grow in the knowledge of the Word<br>• Grow in application of the Word<br>• Grow in bearing fruits of the Word</p><br>
      <p><span style="background:var(--red);color:#fff;font-weight:700;padding:0 2px">STEP FOUR</span><br>We inspire people to FLOURISH.<br>• Flourish in their Faith<br>• Flourish in their missional impact<br>• Flourish in their Occupational impact<br>• Flourish</p>
    </div>
    <div class="abs h" style="left:34px;top:266px;font-size:8px;color:var(--red)">VISION</div>
    <div class="quotebox" style="left:80px;top:256px;width:110px;height:34px;color:#222">
      <div class="h" style="position:absolute;left:8px;top:-13px;font-size:16px">“</div>
      <div style="position:absolute;left:4px;right:4px;top:4px;font:600 6px/8px Montserrat,sans-serif">Flourishing People<br>Planting Flourishing<br>Churches</div>
      <div class="h" style="position:absolute;right:6px;bottom:-15px;font-size:16px">”</div>
    </div>
  </div>
  <div class="redbar"></div>
</section>

<!-- Spread 6: FAQ and get involved -->
<section class="spread faq" style="left:616px;top:812px;background:var(--navy)">
  <div class="photo" role="img" aria-label="Blurred blue toned photo of a congregation facing a stage" style="left:0;top:0;width:476px;height:322px;background:linear-gradient(180deg,#0c1830,#1d3e7a 35%,#0f2244 70%,#3a3342)"></div>
  <span class="runhead" style="left:10px;color:var(--orange)">Riverbend Church</span><span class="runline" style="left:60px;width:356px;background:var(--orange)"></span>
  <span class="runhead" style="left:406px;color:var(--orange)">Riverbend Church</span>
  <div class="abs h" style="left:98px;top:30px;font-size:13px;color:#fff">FAQ</div>
  <div class="abs" style="left:40px;top:72px;width:180px;font-size:3.5px;line-height:4.2px;color:#e6e6e6">
    <p style="color:#f3b53b;font:700 4.2px Montserrat,sans-serif">1) What type of teaching will be employed?</p>
    <p>The teaching model at Riverbend will include multi-ethnic team teaching centered on expository preaching through entire books of the bible.</p><br>
    <p style="color:#f3b53b;font:700 4.2px Montserrat,sans-serif">2) What style of worship can I expect?</p>
    <p>The worship style to be employed at Riverbend will be a unique blend of authentic worship from two or more cultures, including gospel and contemporary music.</p><br>
    <p style="color:#f3b53b;font:700 4.2px Montserrat,sans-serif">3) How long will the service last?</p>
    <p>The typical worship service of Riverbend will last one hour and 15 minutes.</p><br>
    <p style="color:#f3b53b;font:700 4.2px Montserrat,sans-serif">4) How will the church be involved in local outreach?</p>
    <p>Positively impacting the spaces we occupy will be key to who we are. We intend to be at the forefront in serving and partnering with groups already doing great things in our community.</p><br>
    <p style="color:#f3b53b;font:700 4.2px Montserrat,sans-serif">5) What will be the dress code?</p>
    <p>There will be no official dress code to abide by. Feel free to dress comfortably as you attend our services.</p>
  </div>
  <div class="abs" style="left:286px;top:66px;font:400 8px/9px Montserrat,sans-serif;color:var(--orange)">CONSIDER FOUR WAYS<br><b style="font-weight:700">TO GET INVOLVED</b></div>
  <ul class="abs list" style="left:286px;top:90px;font:700 6px/7px Montserrat,sans-serif;color:#fff">
    <li><svg class="tick" style="width:7px;height:7px;flex-basis:7px" viewBox="0 0 10 10"><circle cx="5" cy="5" r="4.3" fill="none" stroke="#fff" stroke-width="1.2"/><path d="M3 5.2l1.5 1.5L7.2 3.6" fill="none" stroke="#fff" stroke-width="1.2"/></svg><span>PRAY</span></li>
    <li><svg class="tick" style="width:7px;height:7px;flex-basis:7px" viewBox="0 0 10 10"><circle cx="5" cy="5" r="4.3" fill="none" stroke="#fff" stroke-width="1.2"/><path d="M3 5.2l1.5 1.5L7.2 3.6" fill="none" stroke="#fff" stroke-width="1.2"/></svg><span>GIVE SACRIFICIALLY</span></li>
    <li><svg class="tick" style="width:7px;height:7px;flex-basis:7px" viewBox="0 0 10 10"><circle cx="5" cy="5" r="4.3" fill="none" stroke="#fff" stroke-width="1.2"/><path d="M3 5.2l1.5 1.5L7.2 3.6" fill="none" stroke="#fff" stroke-width="1.2"/></svg><span>JOIN LAUNCH TEAM</span></li>
    <li><svg class="tick" style="width:7px;height:7px;flex-basis:7px" viewBox="0 0 10 10"><circle cx="5" cy="5" r="4.3" fill="none" stroke="#fff" stroke-width="1.2"/><path d="M3 5.2l1.5 1.5L7.2 3.6" fill="none" stroke="#fff" stroke-width="1.2"/></svg><span>JOIN BEHIND THE SCENES</span></li>
  </ul>
  <div class="abs brand" style="left:300px;top:208px;font-size:17px;color:#fff">Riverbend</div>
  <div class="abs brand" style="left:346px;top:230px;font-size:8px;color:var(--orange);letter-spacing:2px">CHURCH</div>
  <div class="abs" style="left:290px;top:286px;width:120px;text-align:center;font:600 4px/4.8px 'Open Sans',sans-serif;color:#fff">
    <p style="font-size:4.6px">For more Information</p>
    <p>Email: info@riverbendchurch.org</p>
    <p>Phone: 555-014-2290 or visit us at riverbendchurch.org</p>
  </div>
  <div class="abs" style="left:0;bottom:0;width:476px;height:9px;background:var(--orange)"></div>
</section>

</body>
</html>
```